Knightsbridge osteopathy leaflet with a high quality feel for affluent clients

Design a quality flyer for an osteopathy clinic in Knightsbridge.
It must be eye catching, stylish and informative.

To explain the attached documents;
The file’ Marcus Delvanteur Leaflet.pdf’ is approximately what I want, look wise, but with a designer's eye over it - to me this is too amateur.
Logo and background image as well, although I have others if you feel it is not right.
The 'tree logo' is the logo I use for my Richmond clinic; if there is a way to utilise it here then I'm open to it.

Company background;
I am an osteopath hiring a room from an existing business (a hairdresser’s), so I want to capitalise on his success and local name but also make it clear from this leaflet that osteopathy is the focus.

On the back of the flyer, the following copy;

Osteopathy, acupuncture, sports therapy
As well as effective relief from back pain, osteopathy can also provide relief from a variety of problems;
• Shoulder, knee or hip pain
• Arthritic pain
• Tennis / golfer’s elbow
• Sciatica and trapped nerves
• Carpal tunnel syndrome
• Sports injuries and rehab
• Gait analysis
• Postural problems
• Inability to relax / sleep
• Some forms of headache

Address;
Osteopathy at Marcus Delvanteur, 42 Wrenfield Terrace, London, Knightsbridge, NW8 4TJ
Phone; 07914 583027

Target Market(s)

people with back or other pain - sporty, affluent people

Industry/Entity Type

Clinic

Font styles to use
Serif

Requirements
Must have
• eye catching, quality,
Nice to have
• map and directions
• information about osteopathy on the back
Should not have
• a low value feel

```html
<!DOCTYPE html>
<html lang="en">
<head>
<meta charset="utf-8">
<title>Osteopathy at Marcus Delvanteur – Leaflet</title>
<link href="https://fonts.googleapis.com/css2?family=Tinos:wght@400;700&display=swap" rel="stylesheet">
<style>
  :root {
    --gold: #a89d6c;
    --gold-text: #a39a6a;
    --white: #ffffff;
    --map-base: #ededed;
    --map-block: #dcdcdc;
    --pin: #e8892e;
  }
  * { box-sizing: border-box; margin: 0; padding: 0; }
  html, body { width: 852px; height: 1200px; overflow: hidden; background: var(--white); }
  body { font-family: "Tinos", "Times New Roman", serif; color: var(--gold-text); }

  .leaflet { position: relative; width: 852px; height: 1200px; }
  .frame {
    position: absolute; left: 35px; top: 35px; width: 782px; height: 1130px;
    border: 5px solid var(--gold);
  }

  .brand {
    position: absolute; top: 88px; left: 0; width: 852px;
    display: flex; align-items: center; justify-content: center; gap: 12px;
  }
  .brand-dot { width: 34px; height: 34px; border-radius: 50%; background: var(--gold); }
  .brand-name { font-size: 24px; color: var(--gold-text); letter-spacing: 0.5px; }

  .band {
    position: absolute; left: 40px; width: 772px; background: var(--gold); color: var(--white);
  }
  .services-band {
    top: 155px; height: 67px; display: flex; align-items: center; justify-content: center;
    font-size: 30px; letter-spacing: 0.3px;
  }
  .address-band {
    top: 1038px; height: 36px; display: flex; align-items: center; padding-left: 46px;
    font-size: 21px;
  }

  .intro {
    position: absolute; top: 254px; left: 0; width: 852px; text-align: center;
    font-size: 27px; line-height: 33px;
  }

  .conditions {
    position: absolute; top: 344px; left: 118px; display: grid;
    grid-template-columns: 342px 300px; list-style: none;
    font-size: 21px; line-height: 35.5px;
  }
  .conditions li::before { content: "• "; }

  .map-title {
    position: absolute; top: 547px; left: 0; width: 852px; text-align: center; font-size: 28px;
  }

  .map {
    position: absolute; left: 100px; top: 593px; width: 651px; height: 421px;
    background: linear-gradient(160deg, var(--map-base), var(--map-block) 60%, var(--map-base));
  }
  .map-pin { position: absolute; left: 336px; top: 901px; }
  .map-label {
    position: absolute; left: 323px; top: 930px; font-size: 17px; font-weight: 700; color: var(--pin);
  }

  .address {
    position: absolute; top: 1090px; left: 80px; font-size: 17px; line-height: 25px;
  }
</style>
</head>
<body>
<main class="leaflet">
  <div class="frame"></div>

  <header class="brand">
    <span class="brand-dot"></span>
    <span class="brand-name">Delvanteur Osteopathy</span>
  </header>

  <h1 class="band services-band" style="font-weight:400">OSTEOPATHY, ACUPUNCTURE, SPORTS THERAPY</h1>

  <p class="intro">As well as effective relief from back pain, osteopathy<br>can also provide relief from a variety of problems:</p>

  <ul class="conditions">
    <li>Shoulder, knee or hip pain</li>
    <li>Sports injuries and rehab</li>
    <li>Arthritic pain</li>
    <li>Gait analysis</li>
    <li>Tennis / golfer’s elbow</li>
    <li>Postural problems</li>
    <li>Sciatica and trapped nerves</li>
    <li>Inability to relax / sleep</li>
    <li>Carpal tunnel syndrome</li>
    <li>Some forms of headache</li>
  </ul>

  <h2 class="map-title" style="font-weight:400">Where Are We?</h2>
  <div class="map" role="img" aria-label="Street map of the surrounding Knightsbridge streets showing the clinic location"></div>
  <svg class="map-pin" width="18" height="24" viewBox="0 0 18 24" aria-hidden="true">
    <path d="M9 0C4 0 0 4 0 9c0 6 9 15 9 15s9-9 9-15c0-5-4-9-9-9z" fill="var(--pin)"/>
    <circle cx="9" cy="9" r="3.2" fill="#fff"/>
  </svg>
  <span class="map-label">42 Wrenfield Tce</span>

  <div class="band address-band">ADDRESS:</div>
  <address class="address" style="font-style:normal">
    Osteopathy at Marcus Delvanteur, 42 Wrenfield Terrace, Knightsbridge, NW8 4TJ<br>
    Phone: 07914 583027
  </address>
</main>
</body>
</html>
```